Business Card for Bloom Vitality & Strength

Hi can you please design a business card with my logo and program logo (the new one I just sent) somewhere on it too maybe on the back? Needs to be eye catching and super cool.
Trudy Melcombe, Director
Master Personal Trainer & Nutrition Coach
0472 816 305
Www.bloomvitalitystrength.com.au
Insta (logo) bloom_vitality_strength #bloomyou7x72018

Target Market(s)

30+ women looking to change lifestyle to healthy mind body etc

Industry/Entity Type

Health And Wellness

Contact Information for Business Card

As above

Font styles to use
Sans Serif

Colors

Designer to choose colors to be used in the design.

Requirements
Must have
• Must super cool and edgy with a bit of cuteness

```html
<!DOCTYPE html>
<html lang="en">
<head>
<meta charset="utf-8">
<title>Bloom Vitality &amp; Strength – Business Card</title>
<link href="https://fonts.googleapis.com/css2?family=Roboto:wght@400;500;700;900&display=swap" rel="stylesheet">
<style>
  :root {
    --backdrop: #e4e6ea;
    --card: #ffffff;
    --ink: #111111;
    --accent: #c8141c;
    --shadow: rgba(20, 30, 40, 0.18);
  }
  * { margin: 0; padding: 0; box-sizing: border-box; }
  html, body { width: 1200px; height: 788px; overflow: hidden; }
  body {
    background: var(--backdrop);
    font-family: "Roboto", Arial, sans-serif;
    color: var(--ink);
    position: relative;
  }
  .card {
    position: absolute;
    width: 540px;
    height: 320px;
    background: var(--card);
    border-radius: 22px;
    box-shadow: 0 14px 34px var(--shadow);
  }
  .card--front { left: 50px; top: 80px; }
  .card--back { left: 610px; top: 388px; }

  /* Front */
  .brand {
    position: absolute;
    inset: 0;
    display: flex;
    align-items: center;
    justify-content: center;
    gap: 14px;
  }
  .brand__dot {
    width: 34px; height: 34px;
    border-radius: 50%;
    background: var(--accent);
    flex: none;
  }
  .brand__name {
    font-weight: 900;
    font-size: 27px;
    letter-spacing: 0.5px;
    text-transform: uppercase;
    color: var(--ink);
  }

  /* Back */
  .role-title {
    position: absolute;
    top: 36px; right: 34px;
    font-weight: 700;
    font-size: 14px;
  }
  .person {
    position: absolute;
    left: 58px; top: 168px;
  }
  .person__name {
    font-weight: 700;
    font-size: 17px;
    text-transform: uppercase;
    letter-spacing: 0.3px;
  }
  .person__role {
    font-weight: 700;
    font-size: 11px;
    margin-top: 2px;
  }
  .contact {
    list-style: none;
    margin-top: 12px;
  }
  .contact__item {
    display: flex;
    align-items: center;
    gap: 12px;
    font-size: 10.5px;
    font-weight: 500;
    height: 22px;
  }
  .contact__icon { width: 14px; height: 14px; flex: none; }
  .program {
    position: absolute;
    right: 40px; top: 205px;
    display: flex;
    align-items: center;
    gap: 8px;
  }
  .program__dot {
    width: 14px; height: 14px;
    border-radius: 50%;
    background: var(--accent);
  }
  .program__name {
    font-weight: 500;
    font-size: 20px;
    letter-spacing: 1px;
    color: var(--ink);
  }
</style>
</head>
<body>

<section class="card card--front" aria-label="Card front">
  <div class="brand">
    <span class="brand__dot"></span>
    <span class="brand__name">Bloom Vitality &amp; Strength</span>
  </div>
</section>

<section class="card card--back" aria-label="Card back">
  <p class="role-title">Master Personal Trainer &amp; Nutrition Coach</p>

  <div class="person">
    <h1 class="person__name">Trudy Melcombe</h1>
    <p class="person__role">Director</p>
    <ul class="contact">
      <li class="contact__item">
        <svg class="contact__icon" viewBox="0 0 16 16" fill="none" stroke="var(--accent)" stroke-width="1.4" stroke-linejoin="round">
          <path d="M4 1.5l2.2 3-1.4 1.6c.8 1.9 2.2 3.3 4.1 4.1l1.6-1.4 3 2.2-1.3 2.4C6.8 13.2 2.8 9.2 1.6 3.8z"/>
        </svg>
        0472 816 305
      </li>
      <li class="contact__item">
        <svg class="contact__icon" viewBox="0 0 16 16" fill="none" stroke="var(--accent)" stroke-width="1.4" stroke-linejoin="round">
          <rect x="1.5" y="3.5" width="13" height="9"/>
          <path d="M1.5 3.5L8 9l6.5-5.5"/>
        </svg>
        info@bloomvitalitystrength.com.au
      </li>
      <li class="contact__item">
        <svg class="contact__icon" viewBox="0 0 16 16" fill="none" stroke="var(--accent)" stroke-width="1.3">
          <circle cx="8" cy="8" r="6.5"/>
          <ellipse cx="8" cy="8" rx="2.8" ry="6.5"/>
          <path d="M1.5 8h13"/>
        </svg>
        www.bloomvitalitystrength.com.au
      </li>
      <li class="contact__item">
        <svg class="contact__icon" viewBox="0 0 16 16" fill="none" stroke="var(--accent)" stroke-width="1.4">
          <rect x="2" y="2" width="12" height="12" rx="2"/>
        </svg>
        bloom_vitality_strength
      </li>
    </ul>
  </div>

  <div class="program">
    <span class="program__dot"></span>
    <span class="program__name">BloomYou7x7</span>
  </div>
</section>

</body>
</html>
```